tourism marketplace web app redesign*

Hi, I need our front-page redesigned. For the competition please submit a jpg of ABOVE THE FOLD ONLY. The full page redesign will be a revision request. URL is https://qp.vendomix.hu/hu/index.html login:'fullhd' and password:'asdasd' (Fold is supposed to be at "Kiemelt Ajanlatok", use all elements above that. Please use at least one extra color other than the two in the logo, or you may completely change them. FOCUS should be on the central combined search box (3 dropdown, 2 calendar picker + Kereses Button) just like lodgewave.com, staynook.com, Torvil.com, etc... The search box is always large, central, white, we want that too. We want it to look more modern, more clean AND we want to feature a changing beautiful nature photo background (like lodgewave.com).Please use our newly designed logo (in attached pdf) and use that new spelling: "fieldtrek.online"

```html
<!DOCTYPE html>
<html lang="hu">
<head>
<meta charset="utf-8">
<title>fieldtrek.online – Foglalj közvetlen a vadászterületnél</title>
<link href="https://fonts.googleapis.com/css2?family=Open+Sans:wght@400;600;700&display=swap" rel="stylesheet">
<style>
  :root {
    --topbar-bg: #2a2a2a;
    --navbar-bg: #3c3c3c;
    --text-light: #ffffff;
    --text-muted: #c9c9c9;
    --nav-link: #cfcfcf;
    --teal: #5fa896;
    --orange: #f7a81b;
    --orange-dark: #f19a12;
    --field-bg: #ffffff;
    --field-text: #555555;
    --icon-dark: #4a4a4a;
    --divider: #5a5a5a;
  }
  * { box-sizing: border-box; margin: 0; padding: 0; }
  html, body { width: 1200px; height: 614px; overflow: hidden; background: #000; }
  body { font-family: "Open Sans", Arial, sans-serif; color: var(--text-light); }
  a { color: inherit; text-decoration: none; }

  .page { position: relative; width: 1200px; height: 614px; overflow: hidden; }

  /* Top utility bar */
  .topbar {
    position: absolute; left: 0; top: 0; width: 100%; height: 32px;
    background: var(--topbar-bg);
  }
  .topbar-items {
    position: absolute; right: 145px; top: 0; height: 32px;
    display: flex; align-items: center; font-size: 10.5px; color: var(--text-muted);
  }
  .topbar-item { display: flex; align-items: center; gap: 4px; padding: 0 10px; }
  .topbar-item + .topbar-item { border-left: 1px solid var(--divider); height: 18px; }
  .topbar-item:last-child { padding-right: 0; }
  .caret { width: 7px; height: 5px; }

  /* Main navigation */
  .navbar {
    position: absolute; left: 0; top: 32px; width: 100%; height: 80px;
    background: var(--navbar-bg);
  }
  .brand { position: absolute; left: 144px; top: 12px; display: flex; align-items: center; gap: 12px; }
  .brand-mark { width: 56px; height: 56px; border-radius: 50%; background: var(--teal); }
  .brand-name { font-size: 24px; font-weight: 400; color: var(--text-light); letter-spacing: -0.2px; }

  .nav-links { position: absolute; top: 0; height: 80px; left: 0; width: 100%; }
  .nav-link {
    position: absolute; top: 31px; font-size: 12.5px; color: var(--nav-link); white-space: nowrap;
  }
  .nav-link.is-active { color: var(--text-light); }
  .partner-button {
    position: absolute; left: 905px; top: 24px; width: 150px; height: 32px;
    border-radius: 16px; background: var(--teal); color: var(--text-light);
    display: flex; align-items: center; justify-content: center; gap: 6px;
    font-size: 12.5px;
  }
  .partner-button svg { width: 14px; height: 14px; }

  /* Hero */
  .hero { position: absolute; left: 0; top: 112px; width: 100%; height: 502px; }
  .hero-photo {
    position: absolute; inset: 0;
    background:
      radial-gradient(ellipse 420px 200px at 560px 120px, rgba(214,156,64,0.75), rgba(120,80,30,0) 70%),
      radial-gradient(ellipse 700px 320px at 540px 250px, rgba(110,90,40,0.8), rgba(30,28,12,0) 75%),
      linear-gradient(180deg, #3a2a14 0%, #2c2a14 45%, #1a1c0c 75%, #0c0d06 100%);
  }
  .hero-shade {
    position: absolute; inset: 0;
    background:
      linear-gradient(90deg, rgba(0,0,0,0.55) 0%, rgba(0,0,0,0) 22%, rgba(0,0,0,0) 78%, rgba(0,0,0,0.55) 100%),
      linear-gradient(180deg, rgba(0,0,0,0.1) 0%, rgba(0,0,0,0.35) 100%);
  }

  .slide-arrow { position: absolute; top: 240px; width: 18px; height: 26px; }
  .slide-arrow.prev { left: 62px; }
  .slide-arrow.next { left: 1118px; }

  .hero-title {
    position: absolute; left: 0; top: 120px; width: 100%; text-align: center;
    font-size: 34px; font-weight: 700; line-height: 44px;
  }
  .hero-subtitle {
    position: absolute; left: 0; top: 165px; width: 100%; text-align: center;
    font-size: 19.5px; font-weight: 400; line-height: 26px;
  }

  .category-pill {
    position: absolute; top: 206px; height: 31px; border: 2px solid var(--text-light);
    border-radius: 16px; display: flex; align-items: center; justify-content: center;
    font-size: 12px; font-weight: 400; text-transform: uppercase; letter-spacing: 0.1px;
  }

  /* Search box */
  .search-field {
    position: absolute; top: 255px; height: 40px; background: var(--field-bg); border-radius: 2px;
    display: flex; align-items: center; justify-content: space-between;
    padding: 0 13px; color: var(--field-text); font-size: 13.5px;
  }
  .search-field svg { flex: none; }
  .search-button {
    position: absolute; left: 558px; top: 308px; width: 86px; height: 32px; border-radius: 16px;
    background: linear-gradient(180deg, #fbb933, var(--orange-dark));
    color: #2a2012; font-size: 12px; font-weight: 700; border: none;
    display: flex; align-items: center; justify-content: center; font-family: inherit;
  }

  .hero-stats {
    position: absolute; left: 0; top: 357px; width: 100%;
    display: flex; justify-content: center; gap: 24px; font-size: 13px;
  }
  .stat { display: flex; align-items: center; gap: 6px; }
  .stat svg { width: 11px; height: 11px; }
</style>
</head>
<body>
<div class="page">

  <header class="topbar">
    <div class="topbar-items">
      <div class="topbar-item">Large&nbsp;&nbsp;Magyar
        <svg class="caret" viewBox="0 0 10 6"><path d="M0 0h10L5 6z" fill="currentColor"/></svg></div>
      <div class="topbar-item">EUR
        <svg class="caret" viewBox="0 0 10 6"><path d="M0 0h10L5 6z" fill="currentColor"/></svg></div>
      <div class="topbar-item">
        <svg width="11" height="11" viewBox="0 0 12 12"><circle cx="6" cy="3.3" r="3" fill="currentColor"/><path d="M0 12c0-3.5 2.7-5 6-5s6 1.5 6 5z" fill="currentColor"/></svg>
        Regisztráció / Bejelentkezés</div>
    </div>
  </header>

  <nav class="navbar">
    <a class="brand" href="#">
      <span class="brand-mark"></span>
      <span class="brand-name">fieldtrek.online</span>
    </a>
    <div class="nav-links">
      <a class="nav-link is-active" href="#" style="left:490px">Országok</a>
      <a class="nav-link" href="#" style="left:574px">Vadfajok</a>
      <a class="nav-link" href="#" style="left:654px">Rólunk</a>
      <a class="nav-link" href="#" style="left:724px">ÁSZF</a>
      <a class="nav-link" href="#" style="left:782px">Hogyan működik</a>
    </div>
    <a class="partner-button" href="#">
      <svg viewBox="0 0 14 14"><circle cx="7" cy="7" r="7" fill="#fff"/><path d="M7 3.5v7M3.5 7h7" stroke="#5fa896" stroke-width="2"/></svg>
      Legyen PartnerÜnk
    </a>
  </nav>

  <section class="hero">
    <div class="hero-photo" role="img" aria-label="Erdei tisztás naplementében, egy gímszarvas áll a fák között arany fényben"></div>
    <div class="hero-shade"></div>

    <svg class="slide-arrow prev" viewBox="0 0 18 26"><path d="M14 3 5 13l9 10" fill="none" stroke="#fff" stroke-width="4" stroke-linecap="round" stroke-linejoin="round"/></svg>
    <svg class="slide-arrow next" viewBox="0 0 18 26"><path d="M4 3l9 10-9 10" fill="none" stroke="#fff" stroke-width="4" stroke-linecap="round" stroke-linejoin="round"/></svg>

    <h1 class="hero-title">Nincs szükséged vadászatszervezőre!</h1>
    <p class="hero-subtitle">Foglalj közvetlen a vadászterületnél</p>

    <a class="category-pill" href="#" style="left:318px;width:158px">Egyéni vadászatok</a>
    <a class="category-pill" href="#" style="left:486px;width:222px">Társas vadászatok, hajtások</a>
    <a class="category-pill" href="#" style="left:718px;width:166px">Exkluzív csomagok</a>

    <div class="search-field" style="left:145px;width:177px">Összes vad
      <svg width="10" height="6" viewBox="0 0 10 6"><path d="M0 0h10L5 6z" fill="#333"/></svg></div>
    <div class="search-field" style="left:328px;width:178px">Összes ország
      <svg width="10" height="6" viewBox="0 0 10 6"><path d="M0 0h10L5 6z" fill="#333"/></svg></div>
    <div class="search-field" style="left:512px;width:178px">Összes ajánlat
      <svg width="10" height="6" viewBox="0 0 10 6"><path d="M0 0h10L5 6z" fill="#333"/></svg></div>
    <div class="search-field" style="left:695px;width:178px">From
      <svg width="15" height="15" viewBox="0 0 15 15"><rect x="0.75" y="2" width="13.5" height="12.25" fill="none" stroke="#4a4a4a" stroke-width="1.5"/><path d="M0.75 5.5h13.5M4 0v3.5M11 0v3.5M0.75 8.5h13.5M0.75 11.3h13.5M4.2 5.5v8.7M7.5 5.5v8.7M10.8 5.5v8.7" stroke="#4a4a4a" stroke-width="1"/></svg></div>
    <div class="search-field" style="left:878px;width:178px">To
      <svg width="15" height="15" viewBox="0 0 15 15"><rect x="0.75" y="2" width="13.5" height="12.25" fill="none" stroke="#4a4a4a" stroke-width="1.5"/><path d="M0.75 5.5h13.5M4 0v3.5M11 0v3.5M0.75 8.5h13.5M0.75 11.3h13.5M4.2 5.5v8.7M7.5 5.5v8.7M10.8 5.5v8.7" stroke="#4a4a4a" stroke-width="1"/></svg></div>

    <button class="search-button" type="button">KERESES</button>

    <div class="hero-stats">
      <span class="stat"><svg viewBox="0 0 12 12"><path d="M6 0a4 4 0 0 0-4 4c0 3 4 8 4 8s4-5 4-8a4 4 0 0 0-4-4zm0 5.5A1.5 1.5 0 1 1 6 2.5a1.5 1.5 0 0 1 0 3z" fill="#f7a81b"/></svg>123456 terület</span>
      <span class="stat"><svg viewBox="0 0 12 12"><path d="M1 4V1h3M8 1h3v3M11 8v3H8M4 11H1V8" fill="none" stroke="#f7a81b" stroke-width="1.8"/></svg>87654321 ajánlat</span>
      <span class="stat"><svg viewBox="0 0 12 12"><circle cx="5" cy="5" r="3.5" fill="none" stroke="#f7a81b" stroke-width="2"/><path d="M7.5 7.5 11 11" stroke="#f7a81b" stroke-width="2.2" stroke-linecap="round"/></svg>Részletes keresés</span>
    </div>
  </section>

</div>
</body>
</html>
```